Updated Stationary needed using new logo for Hair Tissue Mineral Analysis Company

Simple stationary design needed using new logo!
1. 8.5" x 11" Letterhead with company information listed below
2. 8.5" x 11" Design with Footer only with logo and information for print materials
3. 5.5" x 8.5" letterhead design
4. 4.125" x 9.5" Business envelope (#10 envelope) with address
5. 4.125" x 9.5" Business envelope with clear window (#10 envelope) with address
6. 6.5" x 9.5" envelope (6 3/4 Booklet envelope) with address
7. 10" x 13" Open End envelope
Address:
4817 N. Corwin Street
Phoenix, AZ 85021
Phone:
(602)-417-3926
Website:
www.pexumor.com
Email:
information@pexumor.com
Updates
Need extra days to review
Focused on completing other projects first
Look and feel
Each slider illustrates characteristics of the customer's brand and the style your logo design should communicate.

```html
<!DOCTYPE html>
<html lang="en">
<head>
<meta charset="utf-8">
<title>Pexumor Labs Stationery</title>
<link href="https://fonts.googleapis.com/css2?family=Montserrat:wght@400;600&display=swap" rel="stylesheet">
<style>
:root{
  --backdrop-top:#e4e4e4;
  --backdrop-bottom:#c9c9c9;
  --paper:#ffffff;
  --brand-blue:#2b5ea8;
  --brand-orange:#e8772e;
  --ink:#5a5f66;
  --window:#eceef0;
}
*{margin:0;padding:0;box-sizing:border-box}
html,body{width:841px;height:1200px;overflow:hidden}
body{
  position:relative;
  background:linear-gradient(180deg,var(--backdrop-top),var(--backdrop-bottom));
  font-family:"Montserrat",Arial,sans-serif;
  color:var(--ink);
}
.sheet{
  position:absolute;
  background:var(--paper);
  box-shadow:0 3px 10px rgba(0,0,0,.22);
  overflow:hidden;
}
.brand{
  position:absolute;
  display:flex;align-items:center;gap:5px;
  color:var(--brand-blue);font-weight:600;white-space:nowrap;
}
.brand-mark{display:block;background:var(--brand-blue)}
.brand-lg{font-size:15px}.brand-lg .brand-mark{width:10px;height:10px}
.brand-md{font-size:9px}.brand-md .brand-mark{width:6px;height:6px}
.brand-sm{font-size:6.5px;gap:3px}.brand-sm .brand-mark{width:4px;height:4px}

.contact-row{
  position:absolute;left:0;right:0;
  display:flex;justify-content:center;gap:14px;
  font-size:4.2px;white-space:nowrap;
}
.contact-item{display:flex;align-items:center;gap:2px}
.dot{width:5px;height:5px;border-radius:50%;background:var(--brand-blue)}
.dot-alt{background:var(--brand-orange)}
.band{position:absolute;left:0;right:0;bottom:0;background:var(--brand-blue)}
.return-address{position:absolute;font-size:4.5px;line-height:1.4}
.window{
  position:absolute;background:var(--window);
  border:1px solid #dadde0;border-radius:3px;
}

/* placements */
.letterhead-a{left:34px;top:28px;width:381px;height:499px}
.letterhead-b{left:437px;top:28px;width:376px;height:499px}
.half-letter-a{left:39px;top:538px;width:196px;height:303px}
.half-letter-b{left:264px;top:538px;width:196px;height:303px}
.envelope-window{left:482px;top:538px;width:331px;height:140px}
.envelope-plain{left:482px;top:700px;width:331px;height:141px}
.open-end{left:34px;top:869px;width:431px;height:308px}
.booklet{left:482px;top:869px;width:331px;height:168px}
</style>
</head>
<body>

<section class="sheet letterhead-a" aria-label="Letterhead">
  <div class="brand brand-lg" style="left:22px;top:14px"><span class="brand-mark"></span>Pexumor Labs</div>
  <div class="contact-row" style="bottom:14px">
    <span class="contact-item"><span class="dot"></span>4817 N. Corwin Street Phoenix, AZ 85021</span>
    <span class="contact-item"><span class="dot"></span>(602)-417-3926</span>
    <span class="contact-item"><span class="dot"></span>www.pexumor.com</span>
    <span class="contact-item"><span class="dot"></span>information@pexumor.com</span>
  </div>
</section>

<section class="sheet letterhead-b" aria-label="Letterhead with footer">
  <div class="brand brand-lg" style="left:120px;top:14px"><span class="brand-mark"></span>Pexumor Labs</div>
  <div class="contact-row" style="bottom:14px">
    <span class="contact-item"><span class="dot"></span>4817 N. Corwin Street Phoenix, AZ 85021</span>
    <span class="contact-item"><span class="dot dot-alt"></span>(602)-417-3926</span>
    <span class="contact-item"><span class="dot dot-alt"></span>www.pexumor.com</span>
    <span class="contact-item"><span class="dot"></span>information@pexumor.com</span>
  </div>
</section>

<section class="sheet half-letter-a" aria-label="Half letter letterhead">
  <div class="brand brand-sm" style="left:10px;top:12px"><span class="brand-mark"></span>Pexumor Labs</div>
  <svg style="position:absolute;left:10px;bottom:16px" width="176" height="4" aria-hidden="true">
    <line x1="0" y1="2" x2="176" y2="2" stroke="#c8ccd2" stroke-width=".6"/>
    <circle cx="40" cy="2" r="1.5" fill="#2b5ea8"/><circle cx="80" cy="2" r="1.5" fill="#2b5ea8"/>
    <circle cx="120" cy="2" r="1.5" fill="#2b5ea8"/><circle cx="160" cy="2" r="1.5" fill="#2b5ea8"/>
  </svg>
</section>

<section class="sheet half-letter-b" aria-label="Half letter with footer">
  <div class="brand brand-sm" style="left:10px;top:12px"><span class="brand-mark"></span>Pexumor Labs</div>
  <div class="band" style="height:6px"></div>
  <div class="band" style="height:1px;bottom:9px;background:#c8ccd2"></div>
</section>

<section class="sheet envelope-window" aria-label="Window envelope">
  <div class="return-address" style="left:14px;top:12px">4817 N. Corwin Street<br>Phoenix, AZ 85021</div>
  <div class="window" style="left:36px;top:80px;width:104px;height:32px"></div>
</section>

<section class="sheet envelope-plain" aria-label="Business envelope">
  <div class="brand brand-sm" style="left:14px;top:12px"><span class="brand-mark"></span>Pexumor Labs</div>
  <div class="return-address" style="left:14px;top:23px">4817 N. Corwin Street<br>Phoenix, AZ 85021</div>
</section>

<section class="sheet open-end" aria-label="Open end envelope">
  <div class="brand brand-md" style="left:14px;top:14px;font-size:13px"><span class="brand-mark" style="width:9px;height:9px"></span>Pexumor Labs</div>
  <div class="return-address" style="left:14px;top:34px">4817 N. Corwin Street Phoenix, AZ 85021</div>
  <div class="band" style="height:7px"></div>
</section>

<section class="sheet booklet" aria-label="Booklet envelope">
  <div class="return-address" style="left:14px;top:14px">4817 N. Corwin Street<br>Phoenix, AZ 85021</div>
</section>

</body>
</html>
```